Customer Special Orders Infographic and FAQ

Create a dazzling, unique infographic and FAQ for a new and improved customer special order process being rolled out by Birchpoint Supply.

The infographic should be unique, eye-catching and extremely engaging. Some important notes:

* Needs to be on 8-1/2x11" sheet of paper.
* 1st page is the infographic. 2nd page is the FAQ
* Font size needs to be size 12 or higher.
* You can use the photos I provided to help drive the points, but not necessary to use them.
* Target audience is store owners for Birchpoint Supply. Corporate would like them to use this new program .
* Content for the infographic in the Word document. This is p. 1.
* Content for the FAQ in the PDF - p. 2. IGNORE p. 1 of the PDF.
* See my notes in PDF p. 2, and account for the when creating the PDF
* Use Birchpoint Supply colors in the brochure (red and black)

Target Market(s)

Birchpoint Supply Store Owners

Industry/Entity Type

Retail

Font styles to use
Serif

Colors
EB3D1F
EC4F4E
F09395
F8D3D4
FCEDEE

Requirements
Must have
• Unique, Dazzling, and Eye-Catching!
Should not have
• Old school looking

```html
<!DOCTYPE html>
<html lang="en">
<head>
<meta charset="utf-8">
<title>In-Aisle Customer Special Orders – Birchpoint Supply</title>
<link href="https://fonts.googleapis.com/css2?family=Playfair+Display:wght@700;900&family=Tinos:ital,wght@0,400;0,700;1,400&display=swap" rel="stylesheet">
<style>
  :root {
    --red: #EB3D1F;
    --coral: #EC4F4E;
    --rose: #F09395;
    --blush: #F8D3D4;
    --mist: #FCEDEE;
    --ink: #1c1a1a;
    --rust: #d9483f;
    --paper: #ffffff;
    --backdrop: #ebebeb;
  }
  * { box-sizing: border-box; margin: 0; padding: 0; }
  html, body { width: 1200px; height: 808px; overflow: hidden; background: var(--backdrop); }
  body { font-family: "Tinos", "Times New Roman", serif; color: var(--ink); }

  .flyer {
    position: absolute; left: 303px; top: 20px;
    width: 594px; height: 768px;
    background: var(--paper);
    box-shadow: 0 2px 10px rgba(0,0,0,.12);
    overflow: hidden;
  }

  /* Header */
  .masthead { position: absolute; left: 0; top: 0; width: 594px; height: 157px;
    background: linear-gradient(180deg, #f4f4f4 0%, #ffffff 100%); }
  .brand { position: absolute; left: 38px; top: 74px; display: flex; align-items: center; gap: 6px;
    font-family: "Tinos", serif; font-weight: 700; color: var(--red); }
  .brand-mark { width: 12px; height: 12px; background: var(--red); }
  .brand-name { font-size: 15px; }
  .brand-dept { font-size: 9px; line-height: 1.05; text-transform: uppercase; letter-spacing: .3px;
    padding-left: 6px; border-left: 1px solid var(--red); }
  .title { position: absolute; right: 34px; top: 36px; text-align: right; }
  .title h1 { font-family: "Playfair Display", serif; font-weight: 900; font-size: 58px; line-height: 1; color: var(--ink); }
  .title p { font-family: "Playfair Display", serif; font-weight: 700; font-size: 19px; color: var(--red);
    padding-top: 4px; border-top: 2px solid var(--red); margin-top: 4px; }

  /* Stat panel */
  .stat { position: absolute; left: 0; top: 157px; width: 298px; height: 246px; background: var(--blush); padding: 16px 0 0 24px; }
  .stat-text { width: 150px; font-size: 9px; line-height: 1.35; }
  .stat-figure { font-family: "Tinos", serif; font-weight: 700; font-size: 26px; line-height: 1; margin: 8px 0 8px 8px; }
  .stat-note { font-size: 7px; margin-top: 8px; }
  .stat-art { position: absolute; right: 12px; top: 46px; width: 110px; height: 120px; border-radius: 8px;
    background: linear-gradient(160deg, var(--rose), var(--coral)); }

  /* Goals */
  .goals { position: absolute; left: 298px; top: 157px; width: 296px; height: 246px; padding: 16px 24px 0 22px; background: var(--paper); }
  .goals-intro { font-size: 9px; line-height: 1.35; margin-bottom: 10px; }
  .goals ol { list-style: none; }
  .goals li { display: flex; align-items: center; gap: 10px; font-size: 9px; line-height: 1.3; margin-bottom: 8px;
    padding: 5px 8px; background: var(--mist); border-radius: 6px; box-shadow: 0 1px 3px rgba(0,0,0,.12); }
  .goals .num { flex: 0 0 18px; height: 18px; border-radius: 50%; background: var(--red); color: var(--paper);
    font-size: 9px; font-weight: 700; display: flex; align-items: center; justify-content: center; }

  /* Pathway */
  .pathway { position: absolute; left: 0; top: 403px; width: 298px; height: 318px; background: var(--coral); padding: 14px 18px; color: var(--paper); }
  .pathway h2 { font-size: 9px; font-weight: 400; margin-bottom: 10px; }
  .flow { position: absolute; left: 0; top: 0; }
  .flow-box { position: absolute; background: var(--paper); color: var(--ink); border-radius: 3px;
    font-size: 8px; text-align: center; line-height: 1.2; display: flex; align-items: center; justify-content: center; }
  .flow-box.strong { font-weight: 700; font-size: 9px; }
  .pathway-art { position: absolute; left: 132px; top: 200px; width: 150px; height: 104px; border-radius: 6px;
    background: linear-gradient(160deg, var(--blush), var(--rose)); }

  /* Upgrades */
  .upgrades { position: absolute; left: 298px; top: 403px; width: 296px; height: 318px; background: var(--rust); padding: 14px 22px 0 22px; color: var(--paper); }
  .upgrades-intro { font-size: 9px; line-height: 1.35; margin-bottom: 10px; }
  .upgrades ul { list-style: none; }
  .upgrades li { display: flex; gap: 8px; font-size: 8.5px; line-height: 1.3; margin-bottom: 9px; }
  .upgrades svg { flex: 0 0 11px; margin-top: 1px; }

  /* Footer */
  .contact { position: absolute; left: 0; top: 721px; width: 594px; height: 47px; display: flex; align-items: center; justify-content: center; gap: 70px; font-size: 10px; background: var(--paper); }
  .contact span { display: flex; align-items: center; gap: 8px; }
</style>
</head>
<body>
<main class="flyer">
  <header class="masthead">
    <div class="brand">
      <span class="brand-mark"></span>
      <span class="brand-name">Birchpoint</span>
      <span class="brand-dept">Store Systems &amp;<br>Operations</span>
    </div>
    <div class="title">
      <h1>In-Aisle</h1>
      <p>Customer Special Orders</p>
    </div>
  </header>

  <section class="stat">
    <div class="stat-text">
      <p>The average ticket of a customer special order is</p>
      <p class="stat-figure">&gt; 3x</p>
      <p>larger than that of a regular transaction.* In the same token, consumers are increasingly shopping retail a number of different ways (i.e. in-store pick-up, buying on-line picking up in-store, delivery), and expect brands to have the products they desire.</p>
      <p class="stat-note">* Denotes based on a Birchpoint study</p>
    </div>
    <div class="stat-art" role="img" aria-label="Illustration of a shopper using a large smartphone to place an order"></div>
  </section>

  <section class="goals">
    <p class="goals-intro">To help achieve these expectations, the enhanced customer special order process is now available.</p>
    <ol>
      <li><span class="num">1</span>Reduce the number of steps to execute special orders</li>
      <li><span class="num">2</span>Shorten the time to process orders</li>
      <li><span class="num">3</span>Enable more visibility to order status</li>
      <li><span class="num">4</span>Ultimately provide your customers a better end-to-end experience</li>
    </ol>
  </section>

  <section class="pathway">
    <h2>Pathway to Implementation and training:</h2>
    <svg class="flow" width="298" height="318" viewBox="0 0 298 318" aria-hidden="true">
      <g fill="none" stroke="#ffffff" stroke-width="1.2">
        <path d="M64 66 V80 M60 76 L64 81 L68 76"/>
        <path d="M64 126 V140 M60 136 L64 141 L68 136"/>
        <path d="M64 170 V184 M60 180 L64 185 L68 180"/>
        <path d="M186 72 V80 M182 76 L186 81 L190 76"/>
      </g>
    </svg>
    <div class="flow-box strong" style="left:18px;top:44px;width:92px;height:22px;">BPNET</div>
    <div class="flow-box" style="left:140px;top:40px;width:92px;height:32px;">Birchpoint<br>Learning Place</div>
    <div class="flow-box" style="left:18px;top:82px;width:92px;height:44px;">About Birchpoint –<br>Birchpoint Way of<br>Retailing</div>
    <div class="flow-box" style="left:140px;top:82px;width:92px;height:36px;">Search<br>In-Aisle<br>Special Orders</div>
    <div class="flow-box strong" style="left:18px;top:142px;width:92px;height:28px;">BWOR</div>
    <div class="flow-box" style="left:18px;top:186px;width:92px;height:32px;">Search: In-Aisle<br>Special Orders</div>
    <div class="pathway-art" role="img" aria-label="Illustration of team members studying training materials"></div>
  </section>

  <section class="upgrades">
    <p class="upgrades-intro">This upgrade modernizes and eliminates the existing “pen and paper” approach by syncing up BPNET, your Ledger Desktop system, and the Birchpoint Retailer Mobile app. Doing so, the upgrades include:</p>
    <ul>
      <li><svg width="11" height="11" viewBox="0 0 11 11"><path d="M1.5 5.5 L4.5 8.5 L9.5 2" fill="none" stroke="#fff" stroke-width="1.6"/></svg>New form-filled customer order experience for retail owners and customer priority orders in BPNET</li>
      <li><svg width="11" height="11" viewBox="0 0 11 11"><path d="M1.5 5.5 L4.5 8.5 L9.5 2" fill="none" stroke="#fff" stroke-width="1.6"/></svg>Have integration between the retailer mobile app, BPNET, and Ledger Desktop</li>
      <li><svg width="11" height="11" viewBox="0 0 11 11"><path d="M1.5 5.5 L4.5 8.5 L9.5 2" fill="none" stroke="#fff" stroke-width="1.6"/></svg>Automated customer notifications of order confirmation, pick-up and delivery updates</li>
      <li><svg width="11" height="11" viewBox="0 0 11 11"><path d="M1.5 5.5 L4.5 8.5 L9.5 2" fill="none" stroke="#fff" stroke-width="1.6"/></svg>Promote and track customer order assembly and deliver a higher level of visibility to order status</li>
      <li><svg width="11" height="11" viewBox="0 0 11 11"><path d="M1.5 5.5 L4.5 8.5 L9.5 2" fill="none" stroke="#fff" stroke-width="1.6"/></svg>Eliminate the manual need to create customer order related POs in Ledger Desktop</li>
    </ul>
  </section>

  <footer class="contact">
    <span>
      <svg width="12" height="12" viewBox="0 0 12 12" aria-hidden="true"><path d="M2.5 1 L4.5 1 L5.5 3.8 L4.2 4.8 C4.8 6.3 5.7 7.2 7.2 7.8 L8.2 6.5 L11 7.5 L11 9.5 C11 10.4 10.3 11 9.5 11 C5 10.6 1.4 7 1 2.5 C1 1.7 1.6 1 2.5 1 Z" fill="#1c1a1a"/></svg>
      1 555.014.2290
    </span>
    <span>
      <svg width="14" height="10" viewBox="0 0 14 10" aria-hidden="true"><rect x="0.5" y="0.5" width="13" height="9" fill="#1c1a1a"/><path d="M0.5 0.5 L7 5.5 L13.5 0.5" fill="none" stroke="#fff" stroke-width="1"/></svg>
      storeoperations@birchpointsupply.com
    </span>
  </footer>
</main>
</body>
</html>
```